Landing Page für Beratungszentrum
Zielgruppe
Benötige für ein 'Kornfeld-Beratungszentrum Bau- und Immobilienökonomie' zunächst eine Landing-Page mit Einbindung 'Sachverständiger DIN EN ISO/IEC 17024 für Wertermittlung und Baukostenermittlung und -abrechnung sowie Bauablaufstörung ZERTANO 7-58-4096' sowie Link auf Hochschule (https://www.lxa-campus.de/hochschule/lehrende/ostrander-matthias/)
Nachfolgende Info gemäss Links.
https://www.kornfeld-netz.de/su/7391
https://www.kornfeld-netz.de/de/aktuelles/gruendung-kornfeld-unternehmen.html
Aufgabenstellung
Das Corporate Design von Kornfeld sollte im wesentlichen eingehalten werden. Es gibt ein Logo (beiliegend). Es gibt noch keine eigene Domain (muss noch erfunden werden www.kornfeld-bauoek.xxx; email gibt es matthias.ostrander@kfv-mail.de); rudimentäres Web/Domain Architekt gibt es (moplan.net über webtara). Bild/Bilder nach Abstimmung. Info/Leistungen muss textlich bereinigt werden.
Ein Manual Kornfeld gibt es nicht, nur einige Hinweise im Leitfaden Unternehmenskommunikation (Punkt 7.3, als PDF anbei).

```html
<!DOCTYPE html>
<html lang="de">
<head>
<meta charset="utf-8">
<title>Kornfeld-Beratungszentrum Bau- und Immobilienökonomie</title>
<link rel="stylesheet" href="https://fonts.googleapis.com/css2?family=Barlow:wght@400;500;600;700&family=Barlow+Semi+Condensed:wght@400;500&display=swap">
<style>
  :root {
    --navy: #0b2740;
    --white: #ffffff;
    --ink: #111820;
    --cert-bg: #e7f1f4;
    --cert-line: #2b8aa8;
    --panel: #f3f5f7;
    --photo-a: #3e5a55;
    --photo-b: #c9d3cf;
    --sky-a: #6fa4d8;
    --sky-b: #2f3a44;
  }
  * { box-sizing: border-box; margin: 0; padding: 0; }
  html, body { width: 1200px; height: 1200px; overflow: hidden; background: var(--white); }
  body { font-family: "Barlow", sans-serif; color: var(--ink); }

  .site-header {
    height: 110px;
    display: flex;
    align-items: center;
    justify-content: space-between;
    padding: 0 80px 0 120px;
  }
  .brand { display: flex; align-items: center; gap: 10px; }
  .brand-mark { width: 34px; height: 34px; background: var(--ink); flex: none; }
  .brand-name { font-weight: 600; font-size: 17px; line-height: 19px; color: var(--ink); }
  .main-nav { display: flex; align-items: center; gap: 40px; }
  .main-nav a { font-weight: 500; font-size: 15px; color: var(--ink); text-decoration: none; }
  .main-nav .cta {
    background: var(--navy); color: var(--white);
    padding: 6px 11px; border-radius: 4px; font-weight: 600;
  }

  .hero { display: flex; height: 530px; }
  .hero-copy {
    width: 648px; background: var(--navy); color: var(--white);
    padding: 128px 60px 0 120px;
  }
  .hero-title { font-weight: 600; font-size: 47px; line-height: 56px; margin-bottom: 26px; }
  .hero-text {
    font-family: "Barlow Semi Condensed", sans-serif;
    font-size: 14.5px; line-height: 24px; max-width: 440px;
  }
  .hero-photo {
    flex: 1;
    background: radial-gradient(circle at 65% 65%, var(--photo-b) 0%, #9fb0ab 30%, var(--photo-a) 70%, #2c3f3d 100%);
  }

  .certification { padding: 30px 30px 30px 120px; }
  .cert-box {
    height: 86px; border: 2px solid var(--cert-line); border-radius: 3px;
    background: var(--cert-bg);
    display: flex; align-items: center; justify-content: center; gap: 12px;
  }
  .cert-text { font-weight: 500; font-size: 15px; line-height: 21px; }

  .about-row { display: flex; height: 404px; padding: 0 30px 0 120px; }
  .about-photo {
    width: 580px;
    background: linear-gradient(90deg, var(--sky-a) 0%, #a9c8e6 45%, var(--sky-b) 62%, #556068 100%);
  }
  .about-panel { flex: 1; background: var(--panel); padding: 42px 64px; }
  .about-title { font-weight: 700; font-size: 30px; letter-spacing: 1px; text-transform: uppercase; }
</style>
</head>
<body>
  <header class="site-header">
    <div class="brand">
      <span class="brand-mark"></span>
      <span class="brand-name">Kornfeld-Beratungszentrum<br>Bau- und Immobilienökonomie</span>
    </div>
    <nav class="main-nav">
      <a href="#">Start</a>
      <a href="#">About</a>
      <a href="#">Leistungen</a>
      <a class="cta" href="#">Kontakt aufnehmen</a>
    </nav>
  </header>

  <section class="hero">
    <div class="hero-copy">
      <h1 class="hero-title">Beratung für Bau- &amp;<br>Immobilienökonomie</h1>
      <p class="hero-text">Lorem ipsum dolor sit amet, consetetur sadipscing elitr, sed diam nonumy eirmod tempor invidunt ut labore et dolore magna aliquyam erat, sed diam voluptua. At vero eos et accusam et justo duo dolores et ea rebum. Stet clita kasd gubergren, no sea takimata sanctus es</p>
    </div>
    <div class="hero-photo" role="img" aria-label="Foto: Hand mit Kugelschreiber unterschreibt ein Dokument"></div>
  </section>

  <section class="certification">
    <div class="cert-box">
      <svg width="30" height="36" viewBox="0 0 30 36" aria-hidden="true">
        <path d="M15 2 L27 7 V17 C27 25 21.5 31 15 34 C8.5 31 3 25 3 17 V7 Z" fill="none" stroke="var(--cert-line)" stroke-width="2.6" stroke-linejoin="round"/>
        <path d="M9.5 18 L13.5 22 L21 13.5" fill="none" stroke="var(--cert-line)" stroke-width="2.6" stroke-linecap="round" stroke-linejoin="round"/>
      </svg>
      <p class="cert-text">Sachverständiger DIN EN ISO/IEC 17024 für Wertermittlung<br>und Baukostenermittlung und -abrechnung sowie Bauablaufstörung ZERTANO 7-58-4096</p>
    </div>
  </section>

  <section class="about-row">
    <div class="about-photo" role="img" aria-label="Foto: moderne Gebäudefassade vor blauem Himmel"></div>
    <div class="about-panel">
      <h2 class="about-title">About</h2>
    </div>
  </section>
</body>
</html>
```